Family business needs stationery redesign with new logo

Family owned company, established in 1987 wanting a brand 'refresh'. We are an electrical, refrigeration and construction company based in the Barkly Region Northern Territory, Australia. We have a new logo we would like to use which is uploaded along with our current letterhead and email signature. We are also dropping the word 'contractors' so please do not include this on any designs. Please note also, the 'orange' color used in our logo and designs should be Northern Territory red ochre which is as follows:

RGB (Hex): #C75B12
PantoneĀ® 159 C
CMYK: 1 / 74 / 100 / 7

We are needing our stationery redesigned using our new logo. Please include letterheads, business cards, envelopes, and email signatures.

We currently use our business letterheads for quotations, invoices, letters, HR matters, and internal memos.

We also need a separate simplified letterhead for internal paperwork such as employee leave forms, meeting agendas, and meeting minutes etc.
Updates

Reason: Needing more submissions of full package designs. We are wanting all our stationery, including business cards, letterheads, email signatures, envelopes, etc to be cohesive. We also require ALL the information, as supplied on our template letterhead, to be included on the new letterhead designs. including electrical license no.etc Thank you, K&M

Reason: needing more time as work has got in the way of looking over designs. A lot of designs not meeting the brief/criteria.

Industry/Entity Type

Business

Colors
0355a3
f37122

Requirements
Must have
• The 'orange' color used in the designs should be Northern Territory red ochre which is as follows:
• RGB (Hex): #C75B12
• PantoneĀ® 159 C
• CMYK: 1 / 74 / 100 / 7
• ***MUST INCLUDE ALL INFORMATION THAT IS ON OUR CURRENT LETTERHEAD***
Should not have
• Please do not include the word 'contractors'

```html
<!DOCTYPE html>
<html lang="en">
<head>
<meta charset="utf-8">
<title>K&amp;M Stationery</title>
<link href="https://fonts.googleapis.com/css2?family=Open+Sans:wght@400;600;700&family=Tinos&display=swap" rel="stylesheet">
<style>
:root{
  --navy:#1b2f6e;
  --ochre:#C75B12;
  --paper:#ffffff;
  --ground:#ebebeb;
  --ink:#333333;
}
*{margin:0;padding:0;box-sizing:border-box}
html,body{width:1200px;height:938px;overflow:hidden;background:var(--ground);font-family:"Open Sans",sans-serif;color:var(--ink)}
.canvas{position:relative;width:1200px;height:938px}
.sheet{position:absolute;background:var(--paper);overflow:hidden}
.brand{position:absolute;font-family:"Open Sans",sans-serif;font-weight:700;color:var(--navy);line-height:1;white-space:nowrap}
.services{position:absolute;font-family:"Tinos",serif;color:var(--navy);line-height:1.2}
.contacts{position:absolute;list-style:none;font-size:6.5px;line-height:11.5px}
.contacts li{display:flex;align-items:center;gap:3px}
.dot{width:7px;height:7px;border-radius:50%;background:var(--ochre);display:inline-block}
.rule{position:absolute;left:0;right:0;height:1.5px;background:var(--navy)}
.band{position:absolute;left:0;right:0;background:var(--ochre)}

/* letterhead */
.letterhead{left:184px;top:68px;width:387px;height:544px}
.letter{position:absolute;left:38px;top:137px;width:300px;font-size:5.3px;line-height:8.6px}
.letter p{margin-bottom:8px}
.letter .gap{margin-bottom:22px}
.letter strong{font-weight:700}
.signature{height:26px;width:40px;border-bottom:1px solid #555;margin:4px 0 8px;transform:skewX(-10deg);opacity:.6}
.foot-svg{position:absolute;left:0;top:505px}

/* cover letterhead */
.cover{left:637px;top:42px;width:457px;height:574px}
.cover .brand{left:0;width:457px;text-align:center;top:256px;font-size:50px}
.cover .services{left:0;width:457px;text-align:center;top:323px;font-size:16px;line-height:18.5px}

/* cards */
.card{border-radius:8px}
.card-front{left:46px;top:659px;width:176px;height:99px}
.card-back{left:46px;top:786px;width:176px;height:99px}
.card-lines{position:absolute;font-size:3.8px;line-height:6px}

/* envelopes */
.env-front{left:266px;top:674px;width:431px;height:208px}
.env-back{left:737px;top:674px;width:432px;height:206px}
.flap{position:absolute;left:0;top:0;width:432px;height:70px;background:var(--navy);border-radius:0 0 42px 42px;color:#fff;text-align:center;line-height:70px;font-size:15px;letter-spacing:3px}
.flap b{font-weight:700}
</style>
</head>
<body>
<main class="canvas">

  <section class="sheet letterhead" aria-label="Letterhead">
    <div class="brand" style="left:24px;top:28px;font-size:28px">K&amp;M</div>
    <div class="services" style="left:105px;top:28px;font-size:8.5px">Electrical<br>Refrigeration<br>Building Services</div>
    <ul class="contacts" style="left:300px;top:24px">
      <li><span class="dot"></span>012 345 6789</li>
      <li><span class="dot"></span>012 345 6789</li>
      <li><span class="dot"></span>012 345 6789</li>
      <li><span class="dot"></span>urname@email.com</li>
    </ul>
    <article class="letter">
      <p>July 2, 2012</p>
      <p><strong>Dear CH,</strong><br>ABC Building, def St., Country Name</p>
      <p class="gap">is simply dummy text of the printing and typesetting industry. Lorem Ipsum has been the industry's standard dummy text ever since the 1500s, when an unknown printer took a galley of type and scrambled it to make a type specimen book. It has survived not only five centuries, but also the leap into electronic typesetting, remaining essentially unchanged. It was popularised in the 1960s with the release of Letraset sheets containing Lorem Ipsum passages, and more recently with desktop publishing software like Aldus PageMaker including versions of Lorem Ipsum.</p>
      <p class="gap">is simply dummy text of the printing and typesetting industry. Lorem Ipsum has been the industry's standard dummy text ever since the 1500s, when an unknown printer took a galley of type and scrambled it to make</p>
      <p>is simply dummy text of the printing and typesetting industry. Lorem Ipsum has been the industry's standard dummy text ever since the 1500s, when an unknown printer took a galley of type and scrambled it to make a type specimen book. It has survived not only five centuries, but also the leap into electronic typesetting, remaining essentially unchanged. It was popularised in the 1960s with the release of Letraset sheets containing Lorem Ipsum passages, and more recently with desktop publishing software like Aldus PageMaker including versions of Lorem Ipsum.</p>
      <p>Best Regards,</p>
      <div class="signature" role="img" aria-label="Handwritten signature"></div>
      <p><strong>Dana Price</strong><br>Director<br><br>ABC Building, def St., Country Name</p>
    </article>
    <svg class="foot-svg" width="387" height="39" viewBox="0 0 387 39" aria-hidden="true">
      <path d="M8 3H133L140 16H16Z" fill="var(--navy)"/>
      <path d="M128 3H204L207 16H135Z" fill="var(--ochre)"/>
      <rect x="0" y="14" width="387" height="1.5" fill="var(--navy)"/>
      <rect x="0" y="29" width="387" height="10" fill="var(--ochre)"/>
      <text x="26" y="12" font-family="Open Sans" font-size="5.3" font-weight="700" fill="#fff">083.18th floor,Mall Landline  Road LKG</text>
      <text x="144" y="12" font-family="Open Sans" font-size="4.5" fill="var(--navy)">www.<tspan font-weight="700">YourWebsite</tspan>.com</text>
    </svg>
  </section>

  <section class="sheet cover" aria-label="Simplified letterhead">
    <div class="brand">K&amp;M</div>
    <div class="services">Electrical<br>Refrigeration<br>Building Services</div>
    <svg style="position:absolute;left:0;top:528px" width="457" height="46" viewBox="0 0 457 46" aria-hidden="true">
      <path d="M16 0H160L168 15H26Z" fill="var(--navy)"/>
      <rect x="0" y="14" width="457" height="1.5" fill="var(--navy)"/>
      <rect x="0" y="34" width="457" height="12" fill="var(--ochre)"/>
      <text x="37" y="11" font-family="Open Sans" font-size="7" letter-spacing="1.6" fill="#fff">www.<tspan font-weight="700">YourWebsite</tspan>.com</text>
    </svg>
  </section>

  <section class="sheet card card-front" aria-label="Business card front">
    <div class="brand" style="left:16px;top:16px;font-size:17px">K&amp;M</div>
    <div class="services" style="left:76px;top:15px;font-size:5px">Electrical<br>Refrigeration<br>Building Services</div>
    <svg style="position:absolute;left:0;top:45px" width="176" height="12" viewBox="0 0 176 12" aria-hidden="true">
      <path d="M6 1H80L86 10H10Z" fill="var(--navy)"/>
      <path d="M80 1H122L124 7H84Z" fill="var(--ochre)"/>
      <rect x="0" y="8.5" width="176" height="1" fill="var(--navy)"/>
      <text x="16" y="7.5" font-family="Open Sans" font-size="5.2" font-weight="700" fill="#fff">NED HARLOW</text>
      <text x="87" y="5.5" font-family="Open Sans" font-size="3.4" fill="#fff">Managing Director</text>
    </svg>
    <div class="card-lines" style="left:17px;top:60px">083.18th floor,Mall Landline<br>Road LKG</div>
    <ul class="contacts" style="left:90px;top:62px;font-size:3.8px;line-height:8px">
      <li><span class="dot" style="width:4.5px;height:4.5px"></span>012 345 6789</li>
      <li><span class="dot" style="width:4.5px;height:4.5px"></span>012 345 6789</li>
      <li><span class="dot" style="width:4.5px;height:4.5px"></span>012 345 6789</li>
      <li><span class="dot" style="width:4.5px;height:4.5px"></span>urname@email.com</li>
    </ul>
    <div class="card-lines" style="left:17px;top:87px">www.<b style="color:var(--ochre)">YourWebsite</b>.com</div>
    <div class="band" style="bottom:0;height:4px"></div>
  </section>

  <section class="sheet card card-back" aria-label="Business card back">
    <div class="brand" style="left:52px;top:41px;font-size:17px">K&amp;M</div>
    <div class="services" style="left:104px;top:40px;font-size:5px">Electrical<br>Refrigeration<br>Building Services</div>
  </section>

  <section class="sheet env-front" aria-label="Envelope front">
    <div class="brand" style="left:22px;top:27px;font-size:27px">K&amp;M</div>
    <div class="services" style="left:100px;top:24px;font-size:8.5px">Electrical<br>Refrigeration<br>Building Services</div>
  </section>

  <section class="sheet env-back" aria-label="Envelope back">
    <div class="flap">www.<b>YourWebsite</b>.com</div>
  </section>

</main>
</body>
</html>
```